Marlow Law Stationery - Letterhead, Envelopes, Business Cards

We need high quality business stationery for our Personal Injury Law Firm located in Houston, Texas. The design should include the logo, Marlow Law Group, PLLC, 713-555-4718, 2150 Fernbrook Avenue, Suite 310, Houston, Texas 77019 www.MarlowLaw.example. The colors are blue and white. The letterhead should also include the Attorneys - Tessa Quill, Mitchell R. Marlow and Derek Hale.

```html
<!DOCTYPE html>
<html lang="en">
<head>
<meta charset="utf-8">
<title>Marlow Law Stationery</title>
<link href="https://fonts.googleapis.com/css2?family=Montserrat:wght@400;600;700&family=Lato:wght@400;700&display=swap" rel="stylesheet">
<style>
  :root {
    --navy: #011a3f;
    --paper: #ffffff;
    --backdrop: #e2e3e5;
    --mark-faint: #e3e5ea;
    --ink: #0c1a33;
  }
  * { box-sizing: border-box; margin: 0; padding: 0; }
  html, body { width: 1200px; height: 1047px; overflow: hidden; }
  body {
    position: relative;
    background: var(--backdrop);
    font-family: "Lato", sans-serif;
    color: var(--ink);
  }
  .sheet { position: absolute; background: var(--paper); overflow: hidden; }

  .brand-seal {
    position: absolute;
    border-radius: 50%;
    background: var(--navy);
    border: 2px solid var(--paper);
    outline: 2px solid var(--navy);
    display: flex; align-items: center; justify-content: center;
    text-align: center;
    color: var(--paper);
    font-family: "Montserrat", sans-serif;
    font-weight: 600;
    line-height: 1.1;
  }
  .brand-watermark {
    position: absolute;
    border-radius: 50%;
    background: var(--mark-faint);
    display: flex; align-items: center; justify-content: center;
    text-align: center;
    color: var(--paper);
    font-family: "Montserrat", sans-serif;
    font-weight: 600;
    line-height: 1.05;
  }

  /* Business card front */
  .card-front { left: 53px; top: 50px; width: 344px; height: 186px; }
  .card-front .brand-seal { left: 256px; top: 28px; width: 76px; height: 76px; font-size: 11px; }
  .card-holder { position: absolute; left: 21px; top: 103px; }
  .card-holder .name { font-family: "Montserrat", sans-serif; font-weight: 700; font-size: 13px; color: var(--navy); letter-spacing: .3px; }
  .card-holder .role { font-family: "Montserrat", sans-serif; font-size: 9px; margin-top: 3px; letter-spacing: .2px; }
  .card-rule { position: absolute; left: 21px; top: 137px; width: 306px; height: 1px; background: var(--ink); }
  .card-contacts { position: absolute; left: 21px; top: 143px; font-size: 9px; }
  .card-contacts li { list-style: none; display: flex; align-items: center; gap: 7px; height: 16px; }
  .card-contacts svg { width: 10px; height: 10px; fill: var(--navy); }
  .card-address { position: absolute; right: 22px; top: 146px; font-size: 9px; text-align: right; line-height: 1.3; }
  .card-band { position: absolute; left: 0; bottom: 0; width: 100%; height: 7px; }

  /* Business card back */
  .card-back { left: 53px; top: 255px; width: 333px; height: 185px; background: var(--navy); }
  .card-back .brand-seal { left: 109px; top: 35px; width: 114px; height: 114px; font-size: 16px; outline-color: var(--paper); border-color: var(--navy); }

  /* Letterhead */
  .letterhead { left: 409px; top: 50px; width: 722px; height: 941px; }
  .letterhead .brand-seal { left: 58px; top: 26px; width: 122px; height: 122px; font-size: 18px; }
  .letterhead-firm { position: absolute; left: 205px; top: 44px; width: 240px; }
  .letterhead-firm .firm-name { font-family: "Montserrat", sans-serif; font-weight: 700; font-size: 13px; color: var(--navy); letter-spacing: .3px; }
  .letterhead-firm .attorneys-title { font-family: "Montserrat", sans-serif; font-size: 9px; letter-spacing: 1px; margin-top: 10px; color: var(--navy); }
  .letterhead-firm .attorneys { list-style: none; font-size: 12px; line-height: 1.45; margin-top: 3px; }
  .letterhead-contacts { position: absolute; left: 460px; top: 40px; padding-left: 12px; border-left: 1px solid var(--navy); font-size: 14.5px; line-height: 1.2; }
  .letterhead-contacts li { list-style: none; display: flex; gap: 10px; margin: 4px 0; }
  .letterhead-contacts svg { width: 13px; height: 13px; fill: var(--navy); flex: none; margin-top: 2px; }
  .letterhead .brand-watermark { left: 152px; top: 266px; width: 444px; height: 444px; font-size: 64px; }
  .letterhead-band { position: absolute; left: 0; bottom: 0; width: 100%; height: 24px; }

  /* Envelope */
  .envelope { left: 36px; top: 458px; width: 696px; height: 395px; background: transparent; overflow: visible; }
  .envelope-flap { position: absolute; left: 0; top: 0; width: 696px; height: 93px; }
  .envelope-body { position: absolute; left: 0; top: 92px; width: 696px; height: 303px; background: var(--paper); }
  .envelope .brand-seal { left: 304px; top: 10px; width: 70px; height: 70px; font-size: 10px; outline-color: var(--paper); border-color: var(--navy); }
  .envelope .brand-watermark { left: 225px; top: 126px; width: 246px; height: 246px; font-size: 36px; }
</style>
</head>
<body>

<section class="sheet letterhead">
  <div class="brand-seal">Marlow<br>Law</div>
  <div class="letterhead-firm">
    <p class="firm-name">Marlow Law Group, PLLC</p>
    <p class="attorneys-title">ATTORNEYS</p>
    <ul class="attorneys">
      <li>Tessa Quill</li>
      <li>Mitchell R. Marlow</li>
      <li>Derek Hale</li>
    </ul>
  </div>
  <ul class="letterhead-contacts">
    <li><svg viewBox="0 0 24 24"><path d="M6.6 10.8a15 15 0 0 0 6.6 6.6l2.2-2.2a1 1 0 0 1 1-.25 11.4 11.4 0 0 0 3.6.57 1 1 0 0 1 1 1V20a1 1 0 0 1-1 1A17 17 0 0 1 3 4a1 1 0 0 1 1-1h3.5a1 1 0 0 1 1 1c0 1.25.2 2.450.57 3.57a1 1 0 0 1-.25 1z"/></svg>713-555-4718</li>
    <li><svg viewBox="0 0 24 24"><path d="M12 2a10 10 0 1 0 0 20 10 10 0 0 0 0-20zm-1 17.9A8 8 0 0 1 4.1 11H7v2l4 4zm6.9-2.5A2 2 0 0 0 16 16h-1v-3H9v-2h2V9h2V7h2.5A8 8 0 0 1 17.9 17.4z"/></svg>www.MarlowLaw.example</li>
    <li><svg viewBox="0 0 24 24"><path d="M12 2a7 7 0 0 0-7 7c0 5.2 7 13 7 13s7-7.8 7-13a7 7 0 0 0-7-7zm0 9.5a2.5 2.5 0 1 1 0-5 2.5 2.5 0 0 1 0 5z"/></svg><span>2150 Fernbrook Avenue,<br>Suite 310, Houston, Texas 77019</span></li>
  </ul>
  <div class="brand-watermark">Marlow<br>Law</div>
  <svg class="letterhead-band" viewBox="0 0 722 24" preserveAspectRatio="none">
    <rect width="722" height="24" fill="var(--navy)"/>
    <polygon points="328,0 338,0 372,24 360,24" fill="var(--paper)"/>
  </svg>
</section>

<section class="sheet card-front">
  <div class="brand-seal">Marlow<br>Law</div>
  <div class="card-holder">
    <p class="name">AVERY LINDQVIST</p>
    <p class="role">MANAGING DIRECTOR</p>
  </div>
  <div class="card-rule"></div>
  <ul class="card-contacts">
    <li><svg viewBox="0 0 24 24"><path d="M6.6 10.8a15 15 0 0 0 6.6 6.6l2.2-2.2a1 1 0 0 1 1-.25 11.4 11.4 0 0 0 3.6.57 1 1 0 0 1 1 1V20a1 1 0 0 1-1 1A17 17 0 0 1 3 4a1 1 0 0 1 1-1h3.5a1 1 0 0 1 1 1c0 1.25.2 2.45.57 3.57a1 1 0 0 1-.25 1z"/></svg>713-555-4718</li>
    <li><svg viewBox="0 0 24 24"><path d="M12 2a10 10 0 1 0 0 20 10 10 0 0 0 0-20zm-1 17.9A8 8 0 0 1 4.1 11H7v2l4 4zm6.9-2.5A2 2 0 0 0 16 16h-1v-3H9v-2h2V9h2V7h2.5A8 8 0 0 1 17.9 17.4z"/></svg>www.MarlowLaw.example</li>
  </ul>
  <p class="card-address">2150 Fernbrook Avenue,<br>Suite 310, Houston, Texas 77019</p>
  <svg class="card-band" viewBox="0 0 344 7" preserveAspectRatio="none">
    <rect width="344" height="7" fill="var(--navy)"/>
    <polygon points="180,7 184,7 195,0 190,0" fill="var(--paper)"/>
  </svg>
</section>

<section class="sheet card-back">
  <div class="brand-seal">Marlow<br>Law</div>
</section>

<section class="sheet envelope">
  <svg class="envelope-flap" viewBox="0 0 696 93" preserveAspectRatio="none">
    <polygon points="27,0 668,0 696,93 0,93" fill="var(--navy)"/>
  </svg>
  <div class="envelope-body"></div>
  <div class="brand-seal">Marlow<br>Law</div>
  <div class="brand-watermark">Marlow<br>Law</div>
</section>

</body>
</html>
```